Business Card Design

We need a business card designed which uses our logo and looks really good. The company is called LumaPivot482. We help e-commerce companies reduce cart abandonment by rescuing the sale through our innovative technology.

Our corporate colors are red, black and white.

I have attached our AI file for the logo as well.
Updates

Additional information for the business card:

Name: Derek Malloy
Title: President/CTO
Phone: 1-855-LUMA-482
Website: www.lumapivot482.com
Email: derek@lumapivot482.com

Tag line: Winning Back Every Lost Basket

Industry/Entity Type

E-Commerce

```html
<!DOCTYPE html>
<html lang="en">
<head>
<meta charset="utf-8">
<title>LumaPivot482 — Business Card</title>
<link rel="stylesheet" href="https://fonts.googleapis.com/css2?family=Lato:wght@400;700;900&display=swap">
<style>
  :root {
    --backdrop: #6b6b6b;
    --card-white: #ffffff;
    --brand-red: #e31e24;
    --brand-black: #111111;
    --ink: #1c1c1c;
    --text-light: #ffffff;
  }
  html, body {
    margin: 0;
    padding: 0;
    width: 1200px;
    height: 900px;
    overflow: hidden;
    background: var(--backdrop);
    font-family: "Lato", Arial, sans-serif;
  }
  .stage {
    position: relative;
    width: 1200px;
    height: 900px;
  }
  .card {
    position: absolute;
    left: 180px;
    top: 210px;
    width: 840px;
    height: 480px;
    border-radius: 26px;
    overflow: hidden;
    background: var(--brand-black);
    box-shadow: 0 18px 40px rgba(0,0,0,0.35);
  }
  .card__top {
    height: 176px;
    background: var(--card-white);
    display: flex;
    align-items: center;
    justify-content: center;
    gap: 18px;
  }
  .brand-mark {
    width: 34px;
    height: 34px;
    background: var(--brand-red);
  }
  .brand-name {
    font-weight: 400;
    font-size: 64px;
    letter-spacing: 1px;
    color: var(--ink);
    text-transform: uppercase;
    white-space: nowrap;
  }
  .tagline-band {
    height: 48px;
    background: var(--brand-red);
    display: flex;
    align-items: center;
    justify-content: center;
  }
  .tagline {
    color: var(--text-light);
    font-weight: 700;
    font-size: 21px;
    letter-spacing: 3.5px;
    text-transform: uppercase;
    white-space: nowrap;
  }
  .card__bottom {
    position: relative;
    height: 256px;
  }
  .person {
    position: absolute;
    left: 48px;
    bottom: 58px;
  }
  .person__name {
    color: var(--text-light);
    font-size: 44px;
    line-height: 1;
    font-weight: 400;
    white-space: nowrap;
  }
  .person__name strong { font-weight: 700; }
  .person__title {
    margin-top: 10px;
    color: var(--brand-red);
    font-weight: 700;
    font-size: 19px;
    letter-spacing: 3px;
    text-transform: uppercase;
  }
  .contacts {
    position: absolute;
    left: 488px;
    top: 44px;
    list-style: none;
    margin: 0;
    padding: 0;
  }
  .contact {
    display: flex;
    align-items: center;
    gap: 12px;
    height: 40px;
    color: var(--text-light);
    font-size: 22px;
    white-space: nowrap;
  }
  .contact__badge {
    flex: none;
    width: 28px;
    height: 28px;
    border-radius: 50%;
    background: var(--brand-red);
    color: var(--text-light);
    font-weight: 900;
    font-size: 15px;
    display: flex;
    align-items: center;
    justify-content: center;
  }
</style>
</head>
<body>
  <main class="stage">
    <article class="card">
      <header class="card__top">
        <span class="brand-mark" aria-hidden="true"></span>
        <span class="brand-name">LumaPivot482</span>
      </header>
      <div class="tagline-band">
        <span class="tagline">Winning Back Every Lost Basket</span>
      </div>
      <section class="card__bottom">
        <div class="person">
          <div class="person__name">Derek <strong>Malloy</strong></div>
          <div class="person__title">President/CTO</div>
        </div>
        <ul class="contacts">
          <li class="contact"><span class="contact__badge">P</span>1-855-LUMA-482</li>
          <li class="contact"><span class="contact__badge">W</span>www.lumapivot482.com</li>
          <li class="contact"><span class="contact__badge">E</span>derek@lumapivot482.com</li>
        </ul>
      </section>
    </article>
  </main>
</body>
</html>
```